Inspiring Fundraising Foundation Website to Provide Academic Scholarships

Hello, we are launching a foundation to provide academic scholarships to high school students for college. We'd like this to be an informational website with contact information. There will be a total of approximately 5-7 pages in all.
The color scheme will be purple and white, with a girly feel. I 've attached the logo for reference!

Target Market(s)

high school students, college students

Industry/Entity Type

Education

Coding

Coded - Design and coding required

Number of Pages Required

5+ page

Font styles to use
Serif
Sans Serif
Script

Colors
6b449b
886aae
b7a5cd
e4daeb
ffffff
fdf9cf
fbf289

Requirements
Must have
• Purple, girly feel, to reflect the logo's style. Should be light-themed
Should not have
• No dark themes (aka heavy on black or dark colors)

```html
<!DOCTYPE html>
<html lang="en">
<head>
<meta charset="utf-8">
<title>Aurelia Brooks Foundation</title>
<link rel="stylesheet" href="https://fonts.googleapis.com/css2?family=Courgette&family=Lato:wght@400;700;900&display=swap">
<style>
:root{
  --purple:#4b1d6e;
  --purple-mid:#6b449b;
  --purple-band:#6a3fa0;
  --lilac:#886aae;
  --lilac-soft:#b7a5cd;
  --lilac-pale:#e4daeb;
  --white:#ffffff;
  --ink:#222222;
  --text:#444444;
  --muted:#8a8a8a;
  --grey-bg:#efefef;
  --footer:#1f1f1f;
  --line:#dddddd;
}
*{margin:0;padding:0;box-sizing:border-box}
html,body{width:1200px;height:3600px;overflow:hidden}
body{position:relative;background:var(--white);font-family:"Lato",sans-serif;color:var(--text)}
.abs{position:absolute}
.script{font-family:"Courgette",cursive}

/* header */
.brand{left:78px;top:30px;width:130px;text-align:center;color:var(--purple-mid);font-weight:900;font-size:28px;line-height:30px}
.brand-dot{display:inline-block;width:18px;height:18px;border-radius:50%;background:var(--purple-mid);margin-bottom:4px}
.social-top{top:36px;left:744px;display:flex;gap:10px}
.social-top span{width:42px;height:42px;display:block}
.btn-donate-top{left:950px;top:36px;width:168px;height:44px;background:var(--purple);color:var(--white);font-size:17px;font-weight:700;display:flex;align-items:center;justify-content:center;border-radius:2px}
.nav{top:114px;left:0;width:1200px;height:26px}
.nav a{position:absolute;font-size:17px;font-weight:700;color:var(--ink);text-decoration:none;letter-spacing:.3px}
.nav a.active{color:var(--purple-mid)}
.nav-underline{left:334px;top:146px;width:52px;height:3px;background:var(--purple)}

/* hero */
.hero{left:0;top:168px;width:1200px;height:583px;background:linear-gradient(100deg,#c9b8a6 0%,#e8dfd6 30%,#b5b9b3 55%,#7c8b83 80%,#5f6e69 100%)}
.hero-title{right:82px;top:366px;text-align:right;color:var(--purple);font-size:46px;line-height:58px}
.hero-dots{left:1032px;top:527px;display:flex;gap:8px}
.hero-dots span{width:16px;height:16px;border-radius:50%;border:2px solid var(--white)}
.hero-dots span.on{background:var(--white)}

/* section titles */
.sec-title{left:0;width:1200px;text-align:center;font-size:36px;color:var(--ink)}
.sec-title em{font-style:normal;color:var(--purple-mid)}
.sec-rule{left:558px;width:84px;height:2px;background:#999}

/* about */
.about-text{left:91px;top:890px;width:1018px;font-size:14.5px;line-height:24px;text-align:center;color:var(--text)}
.feature-icon{width:92px;height:92px;border-radius:50%;background:var(--lilac-pale);display:flex;align-items:center;justify-content:center}
.feature-title{font-size:21px;font-weight:700;color:var(--purple-mid)}
.feature-text{font-size:14px;line-height:21px;color:var(--text);width:300px}
.btn-solid{background:var(--purple);color:var(--white);font-weight:700;font-size:16px;display:flex;align-items:center;justify-content:center}
.btn-outline{background:var(--white);color:var(--purple);border:2px solid var(--purple);font-weight:700;font-size:16px;display:flex;align-items:center;justify-content:center}

/* scholarships */
.band{left:0;top:1238px;width:1200px;height:586px;background:var(--purple-band)}
.card{top:1397px;width:310px;height:360px;background:var(--white);border-bottom:4px solid var(--ink)}
.card-photo{width:310px;height:190px}
.card-title{margin-top:22px;text-align:center;font-size:18px;font-weight:700;color:var(--ink)}
.card-text{margin:16px auto 0;width:250px;text-align:center;font-size:13.5px;line-height:20px;color:var(--muted)}
.card-knob{position:absolute;left:137px;bottom:-20px;width:36px;height:36px;border-radius:50%;background:var(--ink)}

/* help */
.help-box{top:2002px;width:228px;height:225px;border:2px solid var(--line);background:var(--white)}
.help-icon{position:absolute;left:74px;top:46px;width:80px;height:70px}
.help-rule{position:absolute;left:92px;top:132px;width:44px;height:2px;background:#bbb}
.help-label{position:absolute;left:0;top:165px;width:100%;text-align:center;font-size:15px;font-weight:700;color:var(--ink)}

/* gallery */
.gallery-bg{left:0;top:2299px;width:1200px;height:701px;background:var(--grey-bg)}
.tile{width:243px;height:221px}
.tile-hover{background:linear-gradient(160deg,#6b449b,#4b2b72);display:flex;flex-direction:column;align-items:center;justify-content:center;color:var(--white)}
.tile-hover .plus{width:56px;height:56px;border:2px solid var(--white);border-radius:50%;display:flex;align-items:center;justify-content:center;font-size:34px;line-height:1}
.tile-hover p{margin-top:26px;font-size:17px}

/* cta */
.cta-line{left:0;width:1200px;text-align:center;font-size:35px;color:var(--ink);line-height:48px}

/* footer */
.footer{left:0;top:3259px;width:1200px;height:288px;background:var(--footer)}
.foot-h{top:3304px;font-size:16px;font-weight:700;color:var(--white);letter-spacing:.4px}
.foot-links{left:79px;top:3345px;list-style:none;font-size:14px;line-height:24.5px;color:#ddd}
.foot-links li::before{content:"›";margin-right:8px}
.contact-row{left:329px;display:flex;gap:12px;font-size:13.5px;line-height:18px;color:#ddd}
.contact-row b{color:var(--white)}
.map{left:643px;top:3355px;width:235px;height:137px;background:linear-gradient(135deg,#cfd8dc,#b9c9b0 50%,#d7dde0);border:3px solid #fff}
.foot-brand{left:958px;top:3340px;width:160px;text-align:center;color:var(--white);font-weight:900;font-size:34px;line-height:38px}
.bottom-bar{left:0;top:3547px;width:1200px;height:53px;background:var(--purple)}
.copyright{left:79px;top:3566px;font-size:13px;color:var(--white)}
.social-foot{left:958px;top:3556px;display:flex;gap:10px}
.social-foot span{width:34px;height:34px;border-radius:50%;border:2px solid var(--white)}
</style>
</head>
<body>

<!-- header -->
<div class="abs brand"><span class="brand-dot"></span><br>Aurelia Brooks Foundation</div>
<div class="abs social-top">
  <span style="background:#3b5998"></span>
  <span style="background:#4db5e8"></span>
  <span style="background:#1a78b4"></span>
  <span style="background:#d93a2b"></span>
</div>
<div class="abs btn-donate-top">DONATE NOW</div>
<nav class="abs nav">
  <a class="active" style="left:334px">HOME</a>
  <a style="left:432px">ABOUT US</a>
  <a style="left:557px">ADVICE AND ASSISTANCE</a>
  <a style="left:806px">FAQ's</a>
  <a style="left:895px">GALLERY</a>
  <a style="left:1013px">CONTACT US</a>
</nav>
<div class="abs nav-underline"></div>

<!-- hero -->
<div class="abs hero" role="img" aria-label="Photo of a smiling student holding a folder on a bright campus"></div>
<div class="abs hero-title script">Helping Those In Need<br>Secure a Better Future</div>
<div class="abs hero-dots"><span class="on"></span><span></span><span></span><span></span></div>

<!-- about -->
<h2 class="abs sec-title script" style="top:792px">About <em>Aurelia Brooks Foundation</em></h2>
<div class="abs sec-rule" style="top:853px"></div>
<p class="abs about-text">Lorem ipsum dolor sit amet, consectetuer adipiscing elit, sed diam nonummy nibh euismod tincidunt ut laoreet dolore magna aliquam erat volutpat. Ut wisi enim ad minim veniam, quis nostrud exerci tation ullamcorper suscipit lobortis nisl ut aliquip ex ea commodo consequat. Duis autem vel eum iriure dolor in hendrerit in vulputate velit esse molestie consequat, vel illum dolore eu feugiat nulla facilisis at vero eros et accumsan et iusto odio dignissim qui blandit praesent luptatum zzril delenit augue duis dolore te feugait nulla facilisi.</p>

<div class="abs feature-icon" style="left:187px;top:1010px">
  <svg width="50" height="50" viewBox="0 0 50 50" fill="none" stroke="#4b1d6e" stroke-width="4"><circle cx="24" cy="26" r="18"/><circle cx="24" cy="26" r="9"/><path d="M24 26 L44 6 M38 6 h6 v6"/></svg>
</div>
<div class="abs feature-title" style="left:295px;top:1020px">Mission</div>
<p class="abs feature-text" style="left:295px;top:1052px">Sed ut perspiciatis unde omnis iste natus error sit voluptatem accusantium dolore.</p>

<div class="abs feature-icon" style="left:609px;top:1010px">
  <svg width="52" height="34" viewBox="0 0 52 34"><path d="M2 17 C14 0 38 0 50 17 C38 34 14 34 2 17Z" fill="#4b1d6e"/><circle cx="26" cy="17" r="9" fill="#e4daeb"/><circle cx="26" cy="17" r="4.5" fill="#4b1d6e"/></svg>
</div>
<div class="abs feature-title" style="left:720px;top:1020px">Vision</div>
<p class="abs feature-text" style="left:720px;top:1052px">Sed ut perspiciatis unde omnis iste natus error sit voluptatem accusantium dolore.</p>

<div class="abs btn-solid" style="left:526px;top:1140px;width:148px;height:41px">READ MORE</div>

<!-- scholarships -->
<section class="abs band"></section>
<h2 class="abs sec-title script" style="top:1294px;color:var(--white)">Scholarship Programs</h2>
<div class="abs sec-rule" style="top:1355px;background:var(--lilac-soft)"></div>

<div class="abs card" style="left:79px">
  <div class="card-photo" role="img" aria-label="Photo of students in a classroom listening to a teacher" style="background:linear-gradient(135deg,#c48f6a,#e4d2c0 55%,#8a6a58)"></div>
  <div class="card-title">Continuing School</div>
  <p class="card-text">Sed ut perspiciatis unde omnis iste natus error sit voluptatem accusantium dolore. perspiciatis unde omnis iste natus .</p>
  <span class="card-knob"></span>
</div>
<div class="abs card" style="left:444px">
  <div class="card-photo" role="img" aria-label="Photo of a student working on a laptop in a library" style="background:linear-gradient(135deg,#6f8a4e,#d9d2c4 55%,#5b4a3e)"></div>
  <div class="card-title">Undergraduate Education</div>
  <p class="card-text">Sed ut perspiciatis unde omnis iste natus error sit voluptatem accusantium dolore. perspiciatis unde omnis iste natus .</p>
  <span class="card-knob"></span>
</div>
<div class="abs card" style="left:809px">
  <div class="card-photo" role="img" aria-label="Photo of graduates in caps and gowns" style="background:linear-gradient(135deg,#8fb7d9,#2a2a2a 60%,#4a4a4a)"></div>
  <div class="card-title">Graduate Program</div>
  <p class="card-text">Sed ut perspiciatis unde omnis iste natus error sit voluptatem accusantium dolore. perspiciatis unde omnis iste natus .</p>
  <span class="card-knob"></span>
</div>

<!-- help -->
<h2 class="abs sec-title script" style="top:1882px">How Could <em>You Help</em> ?</h2>
<div class="abs sec-rule" style="top:1945px"></div>

<div class="abs help-box" style="left:79px">
  <svg class="help-icon" viewBox="0 0 80 70" fill="#4b1d6e"><path d="M4 26 L20 16 L30 22 L44 14 L60 18 L76 28 L70 38 L58 32 L48 44 L40 50 L30 52 L22 44 L10 40Z"/><path d="M30 30 L44 22 L52 28" fill="none" stroke="#fff" stroke-width="2.5"/></svg>
  <div class="help-rule"></div>
  <div class="help-label">SPONSOR A ADULT</div>
</div>
<div class="abs help-box" style="left:350px">
  <svg class="help-icon" viewBox="0 0 80 70" fill="#4b1d6e"><rect x="22" y="8" width="8" height="30" rx="4"/><rect x="36" y="4" width="8" height="34" rx="4"/><rect x="50" y="8" width="8" height="30" rx="4"/><path d="M18 34 H62 L56 66 H24Z"/></svg>
  <div class="help-rule"></div>
  <div class="help-label">BECOME VOLUNTEER</div>
</div>
<div class="abs help-box" style="left:622px">
  <svg class="help-icon" viewBox="0 0 80 70" fill="none" stroke="#4b1d6e" stroke-width="4"><path d="M18 6 H48 L56 14 V64 H18Z"/><path d="M26 28 H44 M26 38 H42 M26 48 H36"/><path d="M46 50 L68 18 L74 22 L52 54 L44 56Z" fill="#4b1d6e"/></svg>
  <div class="help-rule"></div>
  <div class="help-label">ENROL YOUR COLLEGE</div>
</div>
<div class="abs help-box" style="left:890px">
  <svg class="help-icon" viewBox="0 0 80 70" fill="#4b1d6e"><circle cx="46" cy="20" r="14"/><circle cx="46" cy="20" r="6" fill="#fff"/><path d="M10 44 H40 L50 38 H66 V48 L48 60 H10Z"/></svg>
  <div class="help-rule"></div>
  <div class="help-label">SEND DONATION</div>
</div>

<!-- gallery -->
<section class="abs gallery-bg"></section>
<h2 class="abs sec-title script" style="top:2352px">Our <em>Gallery</em></h2>
<div class="abs sec-rule" style="top:2412px"></div>

<div class="abs tile" style="left:79px;top:2477px;background:linear-gradient(135deg,#7a9ab8,#d4c4b0 60%,#5b6f82)" role="img" aria-label="Photo of students walking together outdoors"></div>
<div class="abs tile" style="left:346px;top:2477px;background:linear-gradient(135deg,#f0c98a,#e49a3c 50%,#3a3a3a)" role="img" aria-label="Photo of a graduate holding a diploma"></div>
<div class="abs tile tile-hover" style="left:610px;top:2477px" role="img" aria-label="Gallery photo with a caption overlay"><div class="plus">+</div><p>Lorem Ipsum Dolor Sit</p></div>
<div class="abs tile" style="left:874px;top:2477px;background:linear-gradient(135deg,#b0623e,#e8b9a8 55%,#d94a8a)" role="img" aria-label="Photo of a smiling student with a backpack"></div>
<div class="abs tile" style="left:79px;top:2722px;background:linear-gradient(135deg,#8a5a3a,#e0c090 55%,#5a3a6a)" role="img" aria-label="Photo of a group of students with books"></div>
<div class="abs tile" style="left:346px;top:2722px;background:linear-gradient(180deg,#3f86d1,#6aa8e2 45%,#6b4a3a 46%,#8a5a3e)" role="img" aria-label="Photo of a historic university building"></div>
<div class="abs tile" style="left:610px;top:2722px;background:linear-gradient(135deg,#b7c2a0,#e8dccb 55%,#7a8a6a)" role="img" aria-label="Photo of a student studying with a laptop"></div>
<div class="abs tile" style="left:874px;top:2722px;background:linear-gradient(135deg,#d9d0c0,#f3ede4 55%,#8a7a6a)" role="img" aria-label="Photo of students studying together at a table"></div>

<!-- cta -->
<div class="abs cta-line script" style="top:3040px">Change Their World. Change Yours.</div>
<div class="abs cta-line script" style="top:3088px">This changes everything.</div>
<div class="abs btn-solid" style="left:427px;top:3163px;width:149px;height:41px">APPLY NOW</div>
<div class="abs btn-outline" style="left:614px;top:3163px;width:159px;height:41px">DONATE NOW</div>

<!-- footer -->
<footer class="abs footer"></footer>
<div class="abs foot-h" style="left:79px">QUICK LINKS</div>
<ul class="abs foot-links">
  <li>Home</li><li>About Us</li><li>Advice And Assistance</li><li>FAQ's</li><li>Gallery</li><li>Contact Us</li>
</ul>

<div class="abs foot-h" style="left:329px">CONTACT DETAILS</div>
<div class="abs contact-row" style="top:3352px">
  <svg width="16" height="20" viewBox="0 0 16 20"><path d="M8 0 C3.6 0 0 3.4 0 7.6 C0 13 8 20 8 20 S16 13 16 7.6 C16 3.4 12.4 0 8 0Z" fill="#fff"/><circle cx="8" cy="7.5" r="3" fill="#1f1f1f"/></svg>
  <div><b>Aurelia Brooks Foundation</b><br>123 PG Duis aute irure dolor<br>srephenderit amit in voluptate</div>
</div>
<div class="abs contact-row" style="top:3420px">
  <svg width="16" height="16" viewBox="0 0 16 16"><path d="M3 1 L6 1 L7 5 L5 6.5 C6 9 7 10 9.5 11 L11 9 L15 10 V13 C15 14 14 15 13 15 C6 15 1 10 1 3 C1 2 2 1 3 1Z" fill="#fff"/></svg>
  <b>+ (123) 456 7890</b>
</div>
<div class="abs contact-row" style="top:3450px">
  <svg width="16" height="16" viewBox="0 0 16 16" fill="#fff"><rect x="4" y="1" width="8" height="4"/><rect x="1" y="5" width="14" height="7" rx="1"/><rect x="4" y="10" width="8" height="5" fill="#1f1f1f" stroke="#fff"/></svg>
  <b>+ (123) 456 7890</b>
</div>
<div class="abs contact-row" style="top:3480px">
  <svg width="16" height="12" viewBox="0 0 16 12"><rect width="16" height="12" fill="#fff"/><path d="M0 0 L8 7 L16 0" fill="none" stroke="#1f1f1f" stroke-width="1.5"/></svg>
  <span>info@aureliabrooksfoundation.org</span>
</div>

<div class="abs foot-h" style="left:643px">LOCATION MAP</div>
<div class="abs map" role="img" aria-label="Street map showing the foundation's location"></div>

<div class="abs foot-brand">Aurelia Brooks Foundation</div>

<div class="abs bottom-bar"></div>
<div class="abs copyright">Copyright © 2016 Aurelia Brooks Foundation. All Rights Reserved.</div>
<div class="abs social-foot"><span></span><span></span><span></span><span></span></div>

</body>
</html>
```